Would like a Northwest feel to the look, something NOT typical of what you would see on a typical Home Inspectors logo. Real estate cards all the same as well, and would like to stand out. Earthy, green, Northwest. Sadly a portrait seems to be a requirement (see the attached). I inspect residential homes for buyers and sellers.

Target Market(s)

Home Buyers and Sellers

Industry/Entity Type

Home Inspection

Contact Information for Business Card

See description
Note: The name Corvaneth is a Chinook word that means 'Friend'. Please do not associate the name with the Whale that shows up on 99% of google searches.

Logo Text

Corvaneth Home Inspections

Colors

Designer to choose colors to be used in the design.

Requirements
Must have
• Phone Num: 541-672-8153
• Address: 732 SW 219th Av Num 618
• Portland, Oregon 97388
• Email: glen@corvanethhomeinspection.example
• Website: www.CorvanethHomeInspection.example
• Additional Note: Need to add the Obravex logo (icon). It should be small and not the focus of the card. The logo can be found at Obravex.example
Nice to have
• I am open
Should not have
• Cant think of anything

```html
<!DOCTYPE html>
<html lang="en">
<head>
<meta charset="utf-8">
<title>Corvaneth Home Inspections – Business Card</title>
<link rel="stylesheet" href="https://fonts.googleapis.com/css2?family=Open+Sans:wght@400;600;700&display=swap">
<style>
  :root {
    --canvas: #ffffff;
    --card-dark: #4f4a37;
    --card-light: #ffffff;
    --ink: #231f20;
    --accent-green: #2db36b;
    --on-dark: #ffffff;
    --rule-on-dark: rgba(255, 255, 255, 0.75);
    --badge-ring: #2b2b2b;
    --photo-tone-a: #8c8a5a;
    --photo-tone-b: #5e6448;
  }
  * { box-sizing: border-box; margin: 0; padding: 0; }
  html, body { width: 1200px; height: 927px; overflow: hidden; background: var(--canvas); }
  body { position: relative; font-family: "Open Sans", Arial, sans-serif; }

  .card {
    position: absolute;
    top: 302px;
    width: 540px;
    height: 323px;
    overflow: hidden;
    background: var(--card-dark);
  }
  .card--front { left: 60px; }
  .card--back { left: 600px; }

  .front-curve { position: absolute; inset: 0; }

  .portrait {
    position: absolute;
    left: 52px; top: 74px;
    width: 112px; height: 118px;
    border: 2px solid var(--on-dark);
    background: linear-gradient(160deg, var(--photo-tone-a), var(--photo-tone-b));
  }
  .identity {
    position: absolute;
    left: 33px; top: 199px;
    width: 150px;
    text-align: center;
    color: var(--on-dark);
    font-size: 13.5px;
    line-height: 17px;
  }
  .identity__name { font-weight: 700; font-size: 14px; }

  .cert-badge {
    position: absolute;
    left: 450px; top: 37px;
    width: 52px; height: 52px;
    border-radius: 50%;
    border: 3px solid var(--badge-ring);
    background: var(--card-light);
  }

  .contact-list { list-style: none; }
  .contact-item {
    position: absolute;
    left: 228px;
    display: flex;
    align-items: flex-start;
    color: var(--ink);
    font-size: 13px;
    line-height: 17px;
  }
  .contact-item svg { width: 16px; height: 16px; margin-right: 12px; flex: none; fill: var(--accent-green); }
  .contact-item--address { top: 94px; }
  .contact-item--phone { top: 143px; }
  .contact-item--email { top: 178px; }
  .contact-item--web { top: 216px; }

  .brand {
    position: absolute;
    left: 0; right: 0; top: 128px;
    text-align: center;
    color: var(--on-dark);
    font-weight: 600;
  }
  .brand__name { display: block; font-size: 42px; letter-spacing: 3px; line-height: 46px; text-transform: uppercase; }
  .brand__sub-row {
    display: flex;
    align-items: center;
    justify-content: center;
    gap: 14px;
    margin-top: 10px;
  }
  .brand__rule { width: 56px; height: 1px; background: var(--rule-on-dark); }
  .brand__sub { font-size: 15px; letter-spacing: 3px; text-transform: uppercase; }
</style>
</head>
<body>

<section class="card card--front" aria-label="Business card front">
  <svg class="front-curve" width="540" height="323" viewBox="0 0 540 323" aria-hidden="true">
    <path d="M356 0 C255 8 196 80 196 161 C196 248 262 320 362 323 L540 323 L540 0 Z" fill="var(--card-light)"/>
  </svg>

  <div class="portrait" role="img" aria-label="Portrait photo of the inspector"></div>
  <div class="identity">
    <p class="identity__name">Glen Corvaneth</p>
    <p>Home Inspector</p>
    <p>#000-000</p>
  </div>

  <div class="cert-badge" role="img" aria-label="Certification badge"></div>

  <ul class="contact-list">
    <li class="contact-item contact-item--address">
      <svg viewBox="0 0 16 16" aria-hidden="true"><path d="M8 1 0.5 8h2.2v7h4V10.5h2.6V15h4V8h2.2z"/></svg>
      <span>732 SW 219th Av Num 618<br>Portland, Oregon 97388</span>
    </li>
    <li class="contact-item contact-item--phone">
      <svg viewBox="0 0 16 16" aria-hidden="true"><path d="M3.6 1 6 4.4 4.6 6.2c.9 1.9 2.4 3.4 4.2 4.3l1.8-1.4L14 11.4 12.6 14C6.8 13.6 2.2 9 2 3.3z"/></svg>
      <span>1 (541) 672-8153</span>
    </li>
    <li class="contact-item contact-item--email">
      <svg viewBox="0 0 16 16" aria-hidden="true"><path d="M1 3h14v10H1z M2.5 4.2 8 8.6l5.5-4.4v-.2h-11z" fill-rule="evenodd"/></svg>
      <span>glen@corvanethhomeinspection.example</span>
    </li>
    <li class="contact-item contact-item--web">
      <svg viewBox="0 0 16 16" aria-hidden="true"><circle cx="8" cy="8" r="7"/><path d="M4 4.5c1.5-.5 2.5.5 2.2 1.8-.3 1.2 1.5 1.5 1.2 3-.2 1-1.4 1.2-1.2 2.8M10 2.8c-.5 1.2.5 2 1.6 1.8 1.2-.2 1.6 1 1.3 2" stroke="var(--card-light)" stroke-width="1.3" fill="none"/></svg>
      <span>www.CorvanethHomeInspection.example</span>
    </li>
  </ul>
</section>

<section class="card card--back" aria-label="Business card back">
  <div class="brand">
    <span class="brand__name">Corvaneth</span>
    <div class="brand__sub-row">
      <span class="brand__rule" aria-hidden="true"></span>
      <span class="brand__sub">Home Inspections</span>
      <span class="brand__rule" aria-hidden="true"></span>
    </div>
  </div>
</section>

</body>
</html>
```